Brell Harbor Company Business Cards

Front and Back Business Card - logo and text setup - cool design. I need workable photoshop or illustrator files so I can setup each employee card with design that is created
Updates

Hi everyone, thank you for the great entries. Please no more white and blue cards - there are so many already - black and silver only now please. thanks!

Target Market(s)

Construction Industry - Facility Managers

Industry/Entity Type

Construction

Contact Information for Business Card

I really like contemporary simplistic looks - clean neat....not opposed to seeing some black backrounds

Requirements
Must have
• Logo/website address with design on front only - www.brellharbor-example.com (logo attached)
• Back:
• Name/Title/Company Address/Phone/email address
Nice to have
• Cool design
Should not have
• Nothing gimmicky like Fire or Water - since we are a Fire Protection company - it has all been done

```html
<!DOCTYPE html>
<html lang="en">
<head>
<meta charset="utf-8">
<title>Brell Harbor Company – Business Cards</title>
<link rel="stylesheet" href="https://fonts.googleapis.com/css2?family=Lato:wght@400;700;900&display=swap">
<style>
  :root {
    --backdrop: #3b3b3c;
    --card-dark: #2b2b2d;
    --card-dark-ink: #4a4a4d;
    --card-dark-line: #9a9a9e;
    --card-silver: #d7d8da;
    --ink: #2f2f32;
    --ink-soft: #45464a;
    --accent-silver: #8e9094;
    --accent-black: #1e1e20;
    --silver-light: #e6e7e9;
  }
  * { margin: 0; padding: 0; box-sizing: border-box; }
  html, body { width: 1200px; height: 829px; overflow: hidden; }
  body {
    background: var(--backdrop);
    font-family: "Lato", sans-serif;
    position: relative;
  }
  .card {
    position: absolute;
    top: 282px;
    width: 484px;
    height: 278px;
    overflow: hidden;
  }
  /* Front */
  .card-front { left: 82px; background: var(--card-dark); }
  .card-front .brand-name {
    position: absolute; left: 0; right: 0; top: 112px;
    text-align: center;
    font-weight: 900; font-size: 44px; letter-spacing: -0.5px;
    color: var(--card-dark-ink);
  }
  .card-front .web-row {
    position: absolute; left: 108px; right: 108px; top: 232px;
    display: flex; align-items: center; gap: 7px;
    color: #d6d6d8; font-size: 11.5px; letter-spacing: 1.6px;
  }
  .card-front .web-row .rule { flex: 1; height: 1px; background: var(--card-dark-line); }
  .card-front .web-row b { font-weight: 700; }

  /* Back */
  .card-back { left: 628px; background: var(--card-silver); }
  .card-back .brand-name {
    position: absolute; right: 40px; top: 40px;
    font-weight: 900; font-size: 32px; letter-spacing: -0.5px;
    color: var(--accent-black);
  }
  .card-back .person { position: absolute; left: 37px; top: 113px; }
  .person-name { color: var(--ink); font-weight: 700; font-size: 15px; line-height: 1.2; }
  .person-title { color: var(--ink-soft); font-size: 11.5px; line-height: 1.2; }
  .card-back .divider {
    position: absolute; left: 37px; top: 158px; width: 25px; height: 1px; background: var(--ink-soft);
  }
  .card-back .address {
    position: absolute; left: 37px; top: 172px;
    color: var(--ink-soft); font-size: 11.5px; line-height: 14px;
  }
  .card-back .contacts {
    position: absolute; left: 37px; top: 210px;
    list-style: none; color: var(--ink-soft); font-size: 11.5px; line-height: 14.5px;
  }
  .contacts li { display: flex; align-items: center; gap: 6px; }
  .contacts svg { width: 9px; height: 9px; flex: none; }
  .card-back .swoosh { position: absolute; inset: 0; width: 484px; height: 278px; }
  .card-back .web {
    position: absolute; right: 40px; top: 253px;
    color: var(--silver-light); font-size: 11.5px;
  }
  .card-back .web b { font-weight: 700; }
</style>
</head>
<body>
  <section class="card card-front" aria-label="Card front">
    <div class="brand-name">Brell Harbor</div>
    <div class="web-row"><span class="rule"></span><span>www.<b>brellharbor-example</b>.com</span><span class="rule"></span></div>
  </section>

  <section class="card card-back" aria-label="Card back">
    <svg class="swoosh" viewBox="0 0 484 278" aria-hidden="true">
      <path d="M0 265 C150 262 320 242 420 205 C330 250 170 273 0 278 Z" fill="var(--accent-silver)"/>
      <path d="M484 166 C420 210 300 260 175 278 L484 278 Z" fill="var(--accent-black)"/>
    </svg>
    <div class="brand-name">Brell Harbor</div>
    <div class="person">
      <div class="person-name">Daniel Marsh</div>
      <div class="person-title">Managing Director</div>
    </div>
    <div class="divider"></div>
    <div class="address">Co. Street, Suite, Building<br>City/State, Zip Code</div>
    <ul class="contacts">
      <li>
        <svg viewBox="0 0 10 10" aria-hidden="true"><path d="M2 1 L4 1 L4.6 3 L3.5 3.8 Q4.5 5.8 6.2 6.5 L7 5.4 L9 6 L9 8 Q9 9 8 9 Q1 8.5 1 2 Q1 1 2 1 Z" fill="var(--accent-black)"/></svg>
        300.555.0142
      </li>
      <li>
        <svg viewBox="0 0 10 10" aria-hidden="true"><rect x="0.8" y="2" width="8.4" height="6" fill="none" stroke="var(--accent-black)" stroke-width="1"/><path d="M1 2.3 L5 5.5 L9 2.3" fill="none" stroke="var(--accent-black)" stroke-width="1"/></svg>
        info@brellharbor-example.com
      </li>
    </ul>
    <div class="web">www.<b>brellharbor-example</b>.com</div>
  </section>
</body>
</html>
```